Fahrzeugbeschriftung für Auslieferung von selbst gekochtem Mittagessen an Kindergärten, Schulen, Haushalte und Firmen
Zielgruppe
Wir kochen täglich leckere Mittagessen aus frischen und regionelen Zutaten und liefern diese an Kindergärten, Schulen, Haushalte und Firmen aus.
Mit einem attraktiven Hinguck-Fahrzeug (Voltaro Kargola) auf 3 Seiten beschriftet, wollen wir vor allem Firmenkunden Appetit machen, bei uns anzufragen.
Aufgabenstellung
Das Logo sollte Verwendung finden.
Das Design sollte Appetit machen und eher originell und pfiffig als konservativ sein. Grossflächige Bilder von Essen und/oder Menschen könnten wir uns gut vorstellen.
Ein Spruch, z.B. '...unterwegs im Auftrag des guten Geschmacks' wäre ein guter Claim dazu.
Das Mass der Seitenflächen des Lieferfahrzeuges ist ca. 1,80 x 1,40m (BxH).

```html
<!DOCTYPE html>
<html lang="de">
<head>
<meta charset="utf-8">
<title>KoMahl Mobil – Fahrzeugbeschriftung</title>
<link href="https://fonts.googleapis.com/css2?family=Open+Sans:wght@400;600;700&family=Dancing+Script:wght@500&display=swap" rel="stylesheet">
<style>
  :root{
    --brown:#5a2d14;
    --orange:#e8501c;
    --photo-a:#e2d3c4;
    --photo-b:#b9a593;
    --panel:#ffffff;
    --line:#e3e1de;
    --bg:#f4f3f1;
    --text:#4a3a30;
  }
  *{box-sizing:border-box;margin:0;padding:0}
  html,body{width:1200px;height:848px;overflow:hidden}
  body{background:var(--bg);font-family:"Open Sans",Arial,sans-serif;color:var(--text);position:relative}

  .swatches{position:absolute;left:30px;top:22px;display:flex;gap:6px}
  .swatch{width:72px;height:72px}
  .swatch--brown{background:var(--brown)}
  .swatch--orange{background:var(--orange)}

  .panel{position:absolute;background:var(--panel);border:1px solid var(--line);overflow:hidden}

  .brand{display:flex;flex-direction:column;align-items:flex-start}
  .brand__row{display:flex;align-items:center;gap:8px}
  .brand__dot{width:11px;height:11px;border-radius:50%;background:var(--orange)}
  .brand__name{font-weight:700;color:var(--brown);font-size:26px;line-height:1;white-space:nowrap}
  .brand__tag{font-size:10px;color:var(--orange);margin-top:5px;margin-left:19px;white-space:nowrap}

  .cab{width:250px;height:180px;display:flex;align-items:center;justify-content:center;padding-bottom:28px}
  .cab::after{content:"";position:absolute;left:0;right:0;bottom:0;height:28px;background:var(--brown)}

  .photo-part{position:absolute;top:0;width:230px;height:290px;display:flex;flex-direction:column;align-items:center}
  .photo-area{margin-top:14px;width:200px;height:192px;border-radius:14px;background:linear-gradient(135deg,var(--photo-a),var(--photo-b))}
  .photo-part__web{font-size:16px;color:var(--brown);font-weight:600;line-height:1.2;text-align:center;margin-top:12px}

  .info-part{position:absolute;top:0;width:140px;height:290px;padding:14px 18px 0 18px}
  .claim{font-family:"Dancing Script",cursive;color:var(--brown);font-size:16px;line-height:1.1;margin-bottom:18px}
  .service{display:flex;gap:7px;align-items:flex-start;margin-bottom:20px}
  .service__dot{flex:none;width:13px;height:13px;border-radius:50%;background:var(--brown);border:2px solid var(--orange);margin-top:2px}
  .service__text{font-size:8.5px;line-height:1.3;color:var(--text)}
  .info-part svg{position:absolute;top:0;height:290px;width:16px}

  .divider{position:absolute;top:0;width:1px;height:290px;background:var(--line)}

  .front{width:400px;height:160px;display:flex;align-items:center;justify-content:center}

  .back{width:280px;height:330px}
  .back__swoosh{position:absolute;top:0;height:330px;width:30px}
  .back__brand{position:absolute;left:40px;top:22px}
  .back__brand .brand__name{font-size:19px}
  .back__brand .brand__tag{font-size:8px;margin-left:17px}
  .back__web{position:absolute;left:40px;top:92px;font-size:12px;font-weight:600;color:var(--brown)}
  .back__photo{position:absolute;left:132px;top:112px;width:110px;height:190px;border-radius:12px;background:linear-gradient(135deg,var(--photo-a),var(--photo-b))}
  .back__address{position:absolute;left:40px;top:252px;font-size:7.5px;line-height:1.4;color:var(--brown)}
</style>
</head>
<body>

<div class="swatches">
  <div class="swatch swatch--brown"></div>
  <div class="swatch swatch--orange"></div>
</div>

<!-- left side -->
<div class="panel cab" style="left:40px;top:215px">
  <div class="brand">
    <div class="brand__row"><span class="brand__dot"></span><span class="brand__name">KoMahl Mobil</span></div>
    <span class="brand__tag">Menüservice &amp; Catering</span>
  </div>
</div>

<div class="panel" style="left:300px;top:105px;width:370px;height:290px">
  <div class="photo-part" style="left:0">
    <div class="photo-area" role="img" aria-label="Bildcollage: Fotos von Kindern beim Essen, einer Köchin und Gästen am Mittagstisch über einer Speisen-Illustration"></div>
    <p class="photo-part__web">www.komahl.de<br>Talheim 4 81 36</p>
  </div>
  <div class="divider" style="left:230px"></div>
  <div class="info-part" style="left:230px">
    <svg viewBox="0 0 16 290" preserveAspectRatio="none" style="right:0"><path d="M16 0 C4 80 4 210 16 290 Z" fill="var(--orange)"/></svg>
    <p class="claim">Unterwegs im Auftrag des guten Geschmacks</p>
    <div class="service"><span class="service__dot"></span><span class="service__text">Menüservice für Betriebe, Kitas, Schulen und Haushalte</span></div>
    <div class="service"><span class="service__dot"></span><span class="service__text">Mobiler Mittagstisch an 365 Tagen im Jahr</span></div>
    <div class="service"><span class="service__dot"></span><span class="service__text">Partyservice, Catering, Foodtruck, Equipment</span></div>
  </div>
</div>

<!-- right side -->
<div class="panel" style="left:40px;top:490px;width:370px;height:290px">
  <div class="info-part" style="left:0">
    <svg viewBox="0 0 16 290" preserveAspectRatio="none" style="left:0"><path d="M0 0 C12 80 12 210 0 290 Z" fill="var(--orange)"/></svg>
    <p class="claim">Unterwegs im Auftrag des guten Geschmacks</p>
    <div class="service"><span class="service__dot"></span><span class="service__text">Menüservice für Betriebe, Kitas, Schulen und Haushalte</span></div>
    <div class="service"><span class="service__dot"></span><span class="service__text">Mobiler Mittagstisch an 365 Tagen im Jahr</span></div>
    <div class="service"><span class="service__dot"></span><span class="service__text">Partyservice, Catering, Foodtruck, Equipment</span></div>
  </div>
  <div class="divider" style="left:140px"></div>
  <div class="photo-part" style="left:140px">
    <div class="photo-area" role="img" aria-label="Bildcollage: Fotos von Kindern beim Essen, einer Köchin und Gästen am Mittagstisch über einer Speisen-Illustration"></div>
    <p class="photo-part__web">www.komahl.de<br>Talheim 4 81 36</p>
  </div>
</div>

<div class="panel cab" style="left:420px;top:600px">
  <div class="brand">
    <div class="brand__row"><span class="brand__dot"></span><span class="brand__name">KoMahl Mobil</span></div>
    <span class="brand__tag">Menüservice &amp; Catering</span>
  </div>
</div>

<!-- front -->
<div class="panel front" style="left:760px;top:105px">
  <div class="brand">
    <div class="brand__row"><span class="brand__dot"></span><span class="brand__name">KoMahl Mobil</span></div>
    <span class="brand__tag">Menüservice &amp; Catering</span>
  </div>
</div>

<!-- back -->
<div class="panel back" style="left:820px;top:450px">
  <svg class="back__swoosh" style="left:0" viewBox="0 0 30 330" preserveAspectRatio="none"><path d="M0 0 H22 C8 110 8 220 22 330 H0 Z" fill="var(--orange)"/></svg>
  <svg class="back__swoosh" style="right:0" viewBox="0 0 30 330" preserveAspectRatio="none"><path d="M30 0 H8 C22 110 22 220 8 330 H30 Z" fill="var(--orange)"/></svg>
  <div class="brand back__brand">
    <div class="brand__row"><span class="brand__dot"></span><span class="brand__name">KoMahl Mobil</span></div>
    <span class="brand__tag">Menüservice &amp; Catering</span>
  </div>
  <p class="back__web">www.komahl.de</p>
  <div class="back__photo" role="img" aria-label="Bildcollage: Fotos von Kindern und einer Köchin über einer Speisen-Illustration"></div>
  <p class="back__address">KoMahl Mobil<br>Am Markt 12<br>74388 Talheim</p>
</div>

</body>
</html>
```